New Web Site - Professional Cleaning Company

I want to create a new attractive website that acts as an advertisement to visitors to entice them to reach out for more information.
We are a commercial/business janitorial service - with a new logo, would like the font to be complimentary to the font of logo, as well as the color scheme.
Target Market(s)
Commercial buildings, schools & medical buildings
Industry/Entity Type
Janitorial
Coding
Coded - Design and coding required
Number of Pages Required
4 page
Requirements
Must have
- Professionalism, sharp imagery

```html
<!DOCTYPE html>
<html lang="en">
<head>
<meta charset="utf-8">
<title>Brightwell Facility Services – Website</title>
<link rel="stylesheet" href="https://fonts.googleapis.com/css2?family=Quicksand:wght@500;700&family=Roboto:ital,wght@0,300;0,400;0,500;0,700;1,400&display=swap">
<style>
:root{
  --navy:#1e3d78;
  --sky:#10a2d1;
  --green:#3cb54b;
  --canvas:#e4f2f9;
  --pale:#eef5fc;
  --ink:#3d4656;
  --muted:#8a93a3;
  --line:#dfe4ec;
  --white:#ffffff;
}
*{box-sizing:border-box;margin:0;padding:0}
html,body{width:1200px;height:3734px;overflow:hidden}
body{background:var(--canvas);font-family:"Roboto",sans-serif;color:var(--ink);position:relative}
.head{font-family:"Quicksand",sans-serif;font-weight:700;text-transform:uppercase;letter-spacing:1px}
.eyebrow{font-size:6px;letter-spacing:3px;color:var(--green);text-transform:uppercase;font-weight:500}
.p{font-size:7px;line-height:12px;color:var(--ink)}
.abs{position:absolute}

/* brand board */
.board{position:absolute;top:110px;left:0;width:1200px;height:130px}
.board .brand{position:absolute;left:280px;top:30px;display:flex;align-items:center;gap:10px}
.board .brand .dot{width:46px;height:46px;border-radius:50%;background:var(--navy)}
.board .brand span{font-family:"Quicksand",sans-serif;font-weight:700;font-size:20px;color:var(--navy);line-height:22px}
.board .rule{position:absolute;top:28px;width:1px;height:86px;background:#aab8c8}
.board .label{font-family:"Roboto",sans-serif;font-size:22px;color:var(--navy);font-weight:400}
.board .fonts{position:absolute;left:523px;top:24px}
.board .fonts .q{font-family:"Quicksand",sans-serif;font-weight:700;font-size:18px;color:#1a2233;margin-top:20px}
.board .fonts .r{font-size:15px;color:#566073;margin-top:8px}
.board .colors{position:absolute;left:766px;top:24px}
.board .swatches{display:flex;gap:14px;margin-top:12px}
.board .sw{text-align:center;font-size:9px;color:#566073}
.board .sw i{display:block;width:38px;height:38px;border-radius:50%;margin-bottom:6px}

/* page */
.page{position:absolute;left:230px;top:300px;width:740px;background:var(--white);box-shadow:0 6px 30px rgba(30,61,120,.12)}
section{position:relative;width:740px;overflow:visible}

.topbar{height:16px;background:var(--sky);color:var(--white);font-size:6px;display:flex;align-items:center;padding:0 143px}
.topbar .item{display:flex;align-items:center;gap:3px;margin-right:12px}
.topbar .social{margin-left:auto;display:flex;gap:3px}
.topbar .social i{width:8px;height:8px;border-radius:50%;background:var(--white)}

.nav{height:91px;display:flex;align-items:center;padding:0 146px 0 143px}
.nav .logo{display:flex;align-items:center;gap:6px}
.nav .logo i{width:30px;height:30px;border-radius:50%;background:var(--sky)}
.nav .logo span{font-family:"Quicksand",sans-serif;font-weight:700;font-size:10px;line-height:11px;color:var(--navy)}
.nav .links{margin-left:auto;display:flex;align-items:center;font-size:7px;color:var(--ink)}
.nav .links a{color:inherit;text-decoration:none;padding:0 12px;border-right:1px solid var(--line)}
.nav .links a:last-child{border:none}
.btn{display:inline-flex;align-items:center;justify-content:center;gap:4px;font-size:6px;font-weight:700;color:var(--white);text-transform:uppercase;letter-spacing:.3px}
.nav .btn{background:var(--navy);width:75px;height:25px;margin-left:8px}

.hero{height:339px;background:linear-gradient(100deg,#1e3d78 0%,#23488a 55%,#2b5596 100%)}
.hero .photo{left:380px;top:36px;width:223px;height:303px;background:linear-gradient(180deg,#3c6aa8 0%,#6fb7dc 60%,#9fd3ea 100%)}
.hero .eyebrow{left:143px;top:98px}
.hero h1{position:absolute;left:143px;top:110px;font-size:32px;line-height:36px;color:var(--white);letter-spacing:1px}
.hero .p{position:absolute;left:143px;top:192px;width:230px;color:#c9d6ec}
.hero .btn{position:absolute;left:143px;top:226px;width:64px;height:24px;background:var(--sky)}

.intro{height:285px}
.intro .eyebrow{left:143px;top:45px}
.intro h2{position:absolute;left:143px;top:54px;font-size:15px;color:var(--navy)}
.intro .p1{position:absolute;left:143px;top:84px;width:232px}
.intro .icons{position:absolute;left:143px;top:130px;display:flex;gap:44px}
.intro .icon{text-align:center;font-size:6px;color:var(--green)}
.intro .icon svg{display:block;margin:0 auto 4px}
.intro .p2{position:absolute;left:143px;top:192px;width:232px}
.book{position:absolute;left:412px;top:-36px;width:182px;height:267px;background:var(--white);box-shadow:0 4px 18px rgba(30,61,120,.14);padding:28px 14px 0}
.book h3{font-family:"Quicksand",sans-serif;font-weight:700;font-size:11px;color:var(--sky);text-align:center;margin-bottom:12px}
.book label{display:block;font-size:5.5px;color:var(--ink);margin-bottom:4px}
.book label b{color:var(--sky)}
.book .field{height:14px;border:1px solid var(--line);margin-bottom:12px;font-size:5px;color:var(--muted);padding:4px;display:flex;justify-content:space-between}
.book .btn{width:100%;height:24px;background:var(--navy);margin-top:4px}

.about{height:285px;background:var(--pale)}
.about .circle{left:175px;top:63px;width:160px;height:160px;border-radius:50%;border:6px solid var(--sky);background:linear-gradient(160deg,#d7ecf6,#7eaad0)}
.about svg.arcs{position:absolute;left:146px;top:80px}
.about .eyebrow{left:383px;top:52px}
.about h2{position:absolute;left:383px;top:61px;font-size:15px;color:var(--navy)}
.about .p1{position:absolute;left:383px;top:88px;width:205px}
.about .quote{position:absolute;left:383px;top:128px;width:205px;background:var(--white);border-left:2px solid var(--sky);padding:8px 10px;font-size:7px;line-height:11px;color:var(--navy)}
.about .p2{position:absolute;left:383px;top:188px;width:205px}

.standout{height:526px}
.standout .band{left:0;top:0;width:740px;height:228px;background:var(--sky)}
.standout .eyebrow{left:143px;top:76px;color:#c8ecf8}
.standout h2{position:absolute;left:143px;top:86px;font-size:15px;line-height:19px;color:var(--white)}
.standout .txt{position:absolute;left:369px;top:62px;width:225px;font-size:6.5px;line-height:11px;color:var(--white)}
.standout .txt u{font-weight:700}
.standout .photo{left:369px;top:182px;width:371px;height:210px;background:linear-gradient(135deg,#e9eef2 0%,#bac7d2 55%,#6f8aa5 100%)}
.standout ul{position:absolute;left:143px;top:266px;list-style:none}
.standout li{display:flex;align-items:center;gap:5px;font-size:6.5px;color:var(--sky);height:16px}
.stats{position:absolute;left:143px;top:440px;width:452px;display:flex}
.stat{flex:1;border-right:1px solid var(--line);padding-left:0}
.stat:last-child{border:none}
.stat+.stat{padding-left:14px}
.stat b{display:block;font-family:"Quicksand",sans-serif;font-weight:700;font-size:21px;color:var(--sky)}
.stat span{font-size:5.5px;color:var(--ink)}

.services{height:298px;background:linear-gradient(90deg,#f3f6fa 0%,#f7f9fc 40%,#eef5fc 100%)}
.services .fade{left:0;top:0;width:160px;height:298px;background:linear-gradient(90deg,#dfe6ee,rgba(238,245,252,0))}
.services .eyebrow{left:143px;top:70px}
.services h2{position:absolute;left:143px;top:79px;font-size:15px;color:var(--navy)}
.services .p1{position:absolute;left:143px;top:104px;width:200px}
.services .q{position:absolute;left:143px;top:150px;width:200px;font-size:6.5px;color:var(--sky)}
.services .p2{position:absolute;left:143px;top:166px;width:200px}
.tile{position:absolute;width:96px;height:96px;display:flex;flex-direction:column;align-items:center;justify-content:center;gap:6px;font-size:6.5px;text-align:center;line-height:9px;font-weight:500}
.tile.light{background:var(--white);color:var(--sky)}
.tile.sky{background:var(--sky);color:var(--white)}
.tile.navy{background:var(--navy);color:var(--white)}

.serve{height:291px}
.serve .band{left:0;top:0;width:740px;height:201px;background:var(--navy)}
.serve .eyebrow{left:0;width:740px;text-align:center;top:54px}
.serve h2{position:absolute;left:0;width:740px;text-align:center;top:64px;font-size:15px;color:var(--white)}
.card{position:absolute;top:100px;width:142px;height:191px;background:var(--white);border-bottom:2px solid var(--sky);box-shadow:0 2px 8px rgba(0,0,0,.06);text-align:center}
.card .img{height:101px;margin:4px 4px 0}
.card h4{font-size:7.5px;font-weight:500;color:var(--sky);margin:12px 0 6px}
.card .p{font-size:6.5px;line-height:11px;padding:0 12px}

.process{height:241px}
.process .eyebrow,.video .eyebrow,.testi .eyebrow{left:0;width:740px;text-align:center}
.process .eyebrow{top:56px}
.process h2{position:absolute;left:0;width:740px;text-align:center;top:66px;font-size:15px;color:var(--navy)}
.step{position:absolute;top:116px;width:120px;text-align:center;font-size:6px;color:var(--ink)}
.step .ring{width:60px;height:60px;border-radius:50%;background:var(--sky);border:4px solid #c8ecf8;margin:0 auto 12px;display:flex;align-items:center;justify-content:center;position:relative}
.step .num{position:absolute;top:-8px;left:50%;margin-left:-8px;width:16px;height:16px;border-radius:50%;background:var(--navy);color:var(--white);font-size:6px;display:flex;align-items:center;justify-content:center}
.process .arrow{position:absolute;top:144px;font-size:8px;color:var(--muted)}

.video{height:187px;background:linear-gradient(100deg,#2a4c8c,#1e3d78 45%,#2c5a98)}
.video h2{position:absolute;left:0;width:740px;text-align:center;top:54px;font-size:15px;color:var(--white)}
.video .play{position:absolute;left:349px;top:82px;width:42px;height:42px;border-radius:50%;border:2px solid var(--white);display:flex;align-items:center;justify-content:center}

.testi{height:276px}
.testi .eyebrow{top:56px}
.testi h2{position:absolute;left:0;width:740px;text-align:center;top:66px;font-size:15px;color:var(--navy)}
.testi .quote{position:absolute;left:180px;width:380px;top:96px;text-align:center;font-style:italic;font-size:7px;line-height:14px;color:var(--muted)}
.testi .nav-arrow{position:absolute;top:120px;color:var(--sky);font-size:12px}
.testi .name{position:absolute;left:0;width:740px;text-align:center;top:152px;font-size:7px;font-weight:700;color:var(--sky);letter-spacing:.5px}
.testi .role{position:absolute;left:0;width:740px;text-align:center;top:163px;font-size:5px;color:var(--muted)}
.testi .dots{position:absolute;left:356px;top:186px;display:flex;gap:4px}
.testi .dots i{width:4px;height:4px;border-radius:50%;background:#c7cdd6}
.testi .dots i.on{background:var(--sky)}

.cta{height:214px;background:linear-gradient(90deg,#fff 50%,var(--pale) 50%)}
.cta .photo{left:0;top:0;width:369px;height:214px;background:linear-gradient(135deg,#5f6770,#8d959c 50%,#6a7f93)}
.cta h2{position:absolute;right:144px;top:56px;text-align:right;font-size:15px;line-height:18px;color:var(--navy)}
.cta .btn{position:absolute;right:144px;top:116px;width:80px;height:23px;background:var(--navy)}

.partners{height:107px;background:var(--pale)}
.partners i{position:absolute;top:34px;width:24px;height:24px;border-radius:50%;background:#c5ccd6}
.partners span{position:absolute;top:64px;width:46px;height:4px;background:#d5dbe3;border-radius:2px}

.footer{height:193px;background:var(--navy);color:#c9d6ec}
.footer h5{position:absolute;top:48px;font-family:"Quicksand",sans-serif;font-weight:700;font-size:10px;color:var(--white)}
.footer .p{color:#c9d6ec;font-size:6px;line-height:11px}
.footer ul{list-style:none;font-size:6px;line-height:19px}
.footer .soc{display:flex;gap:4px}
.footer .soc i{width:11px;height:11px;border-radius:50%;background:var(--white)}

.copy{height:21px;background:var(--sky);color:var(--white);font-size:5.5px;display:flex;align-items:center;justify-content:center}
</style>
</head>
<body>

<header class="board">
  <div class="brand"><i class="dot"></i><span>Brightwell<br>Facility Services</span></div>
  <div class="rule" style="left:464px"></div>
  <div class="fonts"><div class="label">Fonts</div><div class="q">Quicksand</div><div class="r">Roboto</div></div>
  <div class="rule" style="left:707px"></div>
  <div class="colors">
    <div class="label">Colors:</div>
    <div class="swatches">
      <div class="sw"><i style="background:var(--navy)"></i>#1e3d78</div>
      <div class="sw"><i style="background:var(--sky)"></i>#10a2d1</div>
      <div class="sw"><i style="background:var(--green)"></i>#3cb54b</div>
    </div>
  </div>
</header>

<main class="page">

  <div class="topbar">
    <span class="item"><svg width="6" height="6" viewBox="0 0 10 10"><path d="M2 1l2 2-1 1.5c.8 1.5 1.6 2.3 3 3L7.5 6l2 2-1.5 1.5C4.5 9 1 5.5.5 2z" fill="#fff"/></svg>+1 555 018 2046</span>
    <span class="item"><svg width="7" height="5" viewBox="0 0 14 10"><rect width="14" height="10" fill="#fff"/><path d="M0 0l7 5 7-5" stroke="#10a2d1" fill="none"/></svg>hello@brightwellfs.com</span>
    <span class="social"><i></i><i></i><i></i></span>
  </div>

  <nav class="nav">
    <div class="logo"><i></i><span>Brightwell<br>Facility Services</span></div>
    <div class="links"><a>About Us</a><a>Services</a><a>Contact</a></div>
    <span class="btn"><svg width="7" height="7" viewBox="0 0 10 10"><path d="M2 1l2 2-1 1.5c.8 1.5 1.6 2.3 3 3L7.5 6l2 2-1.5 1.5C4.5 9 1 5.5.5 2z" fill="#fff"/></svg>Call us now</span>
  </nav>

  <section class="hero">
    <div class="abs photo" role="img" aria-label="Photo of a cleaner in a blue apron holding a handheld vacuum"></div>
    <div class="abs eyebrow">Welcome to Brightwell Facility Services</div>
    <h1 class="head">Janitorial<br>Services</h1>
    <p class="p">We are a professional cleaning company offering all type of cleaning and maintenance services.</p>
    <span class="btn">Our services</span>
  </section>

  <section class="intro">
    <div class="abs eyebrow">Brightwell Facility Services</div>
    <h2 class="head">Introduction</h2>
    <p class="p p1">Lorem ipsum dolor sit amet, consectetur adipiscing elit. Ut elit tellus, luctus nec ullamcorper mattis, pulvinar dapibus leo.</p>
    <div class="icons">
      <div class="icon"><svg width="22" height="22" viewBox="0 0 22 22" fill="none" stroke="#3cb54b" stroke-width="1.2"><path d="M14 2l-5 11M6 13h8l2 7H4z"/><path d="M8 16v4M12 16v4"/></svg>Sweeping</div>
      <div class="icon"><svg width="22" height="22" viewBox="0 0 22 22" fill="none" stroke="#3cb54b" stroke-width="1.2"><path d="M11 2v12M5 14h12l1 6H4z"/><path d="M7 17h8"/></svg>Mopping</div>
      <div class="icon"><svg width="22" height="22" viewBox="0 0 22 22" fill="none" stroke="#3cb54b" stroke-width="1.2"><rect x="6" y="8" width="8" height="12" rx="1"/><path d="M8 8V4h5l3 2M16 3l3-1M16 6h3"/></svg>Cleaning</div>
    </div>
    <p class="p p2">Lorem ipsum dolor sit amet, consectetur adipiscing elit. Ut elit tellus, luctus nec ullamcorper mattis, pulvinar dapibus leo.</p>

    <form class="book">
      <h3>Book a Service</h3>
      <label>Full Name <b>*</b></label><div class="field"></div>
      <label>Email <b>*</b></label><div class="field"></div>
      <label>Phone Number <b>*</b></label><div class="field"></div>
      <label>Choose a Service <b>*</b></label><div class="field"><span>Commercial Building Cleaning</span><span>▾</span></div>
      <span class="btn">Submit details ➔</span>
    </form>
  </section>

  <section class="about">
    <svg class="arcs" width="216" height="126" viewBox="0 0 216 126" fill="none" stroke="#3cb54b" stroke-width="2.5"><path d="M14 10 Q-4 63 14 116"/><path d="M202 10 Q220 63 202 116"/></svg>
    <div class="abs circle" role="img" aria-label="Photo of the cleaning team in uniforms and aprons"></div>
    <div class="abs eyebrow">Who we are</div>
    <h2 class="head">About us</h2>
    <p class="p p1">Lorem ipsum dolor sit amet, consectetur adipiscing elit. Ut elit tellus, luctus nec ullamcorper mattis, pulvinar dapibus leo.</p>
    <div class="quote">Local operations team on-call 24 hours a day, available to work at a moment's notice.</div>
    <p class="p p2">Ut enim ad minim veniam, quis nostrud exercitation ullamco laboris nisi ut aliquip ex ea commodo consequat. Duis aute irure dolor in reprehenderit in voluptate velit.</p>
  </section>

  <section class="standout">
    <div class="abs band"></div>
    <div class="abs eyebrow">Smooth cleaning experience</div>
    <h2 class="head">What makes us<br>stand out</h2>
    <div class="txt">Temporibus autem quibusdam et aut officiis debitis aut rerum necessitatibus <u>saepe eveniet ut et voluptates repudiandae sint</u> et molestiae non recusandae.<br><br>Ut enim ad minim veniam, quis nostrud exercitation ullamco laboris nisi ut aliquip ex ea commodo consequat. Duis aute irure dolor in reprehenderit in voluptate velit.</div>
    <div class="abs photo" role="img" aria-label="Photo of cleaners disinfecting desks in an open-plan office"></div>
    <ul>
      <li><svg width="7" height="7" viewBox="0 0 10 10"><circle cx="5" cy="5" r="5" fill="#10a2d1"/><path d="M3 5l1.5 1.5L7 3.5" stroke="#fff" fill="none"/></svg>Some text filler for design purposes only</li>
      <li><svg width="7" height="7" viewBox="0 0 10 10"><circle cx="5" cy="5" r="5" fill="#10a2d1"/><path d="M3 5l1.5 1.5L7 3.5" stroke="#fff" fill="none"/></svg>Some text filler for design purposes only</li>
      <li><svg width="7" height="7" viewBox="0 0 10 10"><circle cx="5" cy="5" r="5" fill="#10a2d1"/><path d="M3 5l1.5 1.5L7 3.5" stroke="#fff" fill="none"/></svg>Some text filler for design purposes only</li>
      <li><svg width="7" height="7" viewBox="0 0 10 10"><circle cx="5" cy="5" r="5" fill="#10a2d1"/><path d="M3 5l1.5 1.5L7 3.5" stroke="#fff" fill="none"/></svg>Some text filler for design purposes only</li>
      <li><svg width="7" height="7" viewBox="0 0 10 10"><circle cx="5" cy="5" r="5" fill="#10a2d1"/><path d="M3 5l1.5 1.5L7 3.5" stroke="#fff" fill="none"/></svg>Some text filler for design purposes only</li>
      <li><svg width="7" height="7" viewBox="0 0 10 10"><circle cx="5" cy="5" r="5" fill="#10a2d1"/><path d="M3 5l1.5 1.5L7 3.5" stroke="#fff" fill="none"/></svg>Some text filler for design purposes only</li>
    </ul>
    <div class="stats">
      <div class="stat"><b>+10</b><span>Years of experience</span></div>
      <div class="stat"><b>23</b><span>Team Professionals</span></div>
      <div class="stat"><b>8123</b><span>Square Feet Cleaned</span></div>
      <div class="stat"><b>687</b><span>Satisfied Customers</span></div>
    </div>
  </section>

  <section class="services">
    <div class="abs fade" role="img" aria-label="Faint photo of a cleaning cart in a hallway"></div>
    <div class="abs eyebrow">What we offer</div>
    <h2 class="head">Services</h2>
    <p class="p p1">Quis autem vel eum iure reprehenderit qui in ea voluptate velit esse quam nihil molestiae consequatur, vel illum qui dolorem eum fugiat quo voluptas nulla pariatur.</p>
    <p class="q">"Et harum quidem rerum facilis est et expedita distinctio"</p>
    <p class="p p2">Neque porro quisquam est, qui dolorem ipsum quia dolor sit amet, consectetur adipisci velit sed quia numquam.</p>
    <div class="tile light" style="left:383px;top:50px"><svg width="20" height="20" viewBox="0 0 20 20" fill="none" stroke="#10a2d1" stroke-width="1.2"><path d="M10 3l7 4-7 4-7-4z"/><path d="M3 11l7 4 7-4"/></svg>Floor/Tiles<br>Cleanup</div>
    <div class="tile sky" style="left:490px;top:50px"><svg width="20" height="20" viewBox="0 0 20 20" fill="none" stroke="#fff" stroke-width="1.2"><rect x="4" y="3" width="12" height="14"/><path d="M10 3v14M4 10h12"/></svg>Windows Full<br>Cleanup</div>
    <div class="tile navy" style="left:383px;top:151px"><svg width="20" height="20" viewBox="0 0 20 20" fill="none" stroke="#fff" stroke-width="1.2"><rect x="3" y="3" width="14" height="10"/><path d="M3 8h14M8 3v5M12 8v5M7 13v4h6v-4"/></svg>Wall &amp; Ceiling<br>Cleaning</div>
    <div class="tile light" style="left:490px;top:151px"><svg width="20" height="20" viewBox="0 0 20 20" fill="none" stroke="#10a2d1" stroke-width="1.2"><path d="M4 17h12M6 17V7h6v10M12 10h3v7M8 9h2M8 12h2"/></svg>Full Cleanup<br>Maintenance</div>
  </section>

  <section class="serve">
    <div class="abs band"></div>
    <div class="abs eyebrow">Whom we serve</div>
    <h2 class="head">Who we serve</h2>
    <div class="card" style="left:143px"><div class="img" role="img" aria-label="Photo of a floor scrubbing machine in a commercial building" style="background:linear-gradient(160deg,#b7c6d3,#3f5f86)"></div><h4>Commercial Buildings</h4><p class="p">Lorem ipsum dolor sit amet, consectetur adipiscing elit. Ut elit tellus, luctus nec ullamcorper mattis, pulvinar dapibus leo.</p></div>
    <div class="card" style="left:297px"><div class="img" role="img" aria-label="Photo of a cleaner mopping a hospital corridor" style="background:linear-gradient(160deg,#d4e6f2,#7fa3c8)"></div><h4 style="color:var(--navy)">Medical Buildings</h4><p class="p">Lorem ipsum dolor sit amet, consectetur adipiscing elit. Ut elit tellus, luctus nec ullamcorper mattis, pulvinar dapibus leo.</p></div>
    <div class="card" style="left:452px"><div class="img" role="img" aria-label="Photo of gloved hands wiping a school desk" style="background:linear-gradient(160deg,#c9dde8,#5a8cb0)"></div><h4>Schools</h4><p class="p">Lorem ipsum dolor sit amet, consectetur adipiscing elit. Ut elit tellus, luctus nec ullamcorper mattis, pulvinar dapibus leo.</p></div>
  </section>

  <section class="process">
    <div class="abs eyebrow">How it works</div>
    <h2 class="head">The process</h2>
    <div class="step" style="left:118px"><div class="ring"><span class="num">01</span><svg width="22" height="22" viewBox="0 0 22 22" fill="none" stroke="#fff" stroke-width="1.3"><rect x="5" y="3" width="12" height="16" rx="1"/><path d="M8 8h6M8 12h6M8 16h3"/></svg></div>Choose Service</div>
    <div class="abs arrow" style="left:266px">→</div>
    <div class="step" style="left:309px"><div class="ring"><span class="num">02</span><svg width="22" height="22" viewBox="0 0 22 22" fill="none" stroke="#fff" stroke-width="1.3"><path d="M5 3l3 3-1.5 2c1 2 2.5 3.5 4.5 4.5L13 11l3 3-2 2C8 15.5 5 12 4.5 6z"/><path d="M13 3h6v5h-3l-2 2V8h-1z"/></svg></div>Reach for Us</div>
    <div class="abs arrow" style="left:456px">→</div>
    <div class="step" style="left:499px"><div class="ring"><span class="num">03</span><svg width="22" height="22" viewBox="0 0 22 22" fill="none" stroke="#fff" stroke-width="1.3"><path d="M5 17l8-8M13 9l2-4 2 2-4 2z"/><path d="M6 5v3M4.5 6.5h3M16 14v3M14.5 15.5h3"/></svg></div>Enjoy the Neat</div>
  </section>

  <section class="video" role="img" aria-label="Faint background photo of cleaning staff at work">
    <h2 class="head">See how we do it</h2>
    <div class="play"><svg width="10" height="10" viewBox="0 0 10 10"><path d="M2 1l7 4-7 4z" fill="#fff"/></svg></div>
  </section>

  <section class="testi">
    <div class="abs eyebrow">What our clients say</div>
    <h2 class="head">Testimonials</h2>
    <p class="quote">I am slide content. Click edit button to change this text. Lorem ipsum dolor sit amet, consectetur adipiscing elit. Ut elit tellus, luctus nec ullamcorper mattis, pulvinar dapibus leo. Add some more text filler for design purposes.</p>
    <span class="nav-arrow" style="left:146px">‹</span>
    <span class="nav-arrow" style="left:588px">›</span>
    <div class="name">CLARA MOSS</div>
    <div class="role">CEO</div>
    <div class="dots"><i></i><i class="on"></i><i></i></div>
  </section>

  <section class="cta">
    <div class="abs photo" role="img" aria-label="Overhead photo of cleaners mopping and vacuuming an office floor"></div>
    <h2 class="head">Need janitorial<br>services?</h2>
    <span class="btn"><svg width="7" height="7" viewBox="0 0 10 10"><path d="M2 1l2 2-1 1.5c.8 1.5 1.6 2.3 3 3L7.5 6l2 2-1.5 1.5C4.5 9 1 5.5.5 2z" fill="#fff"/></svg>Give us a call</span>
  </section>

  <section class="partners" aria-label="Partner badges">
    <i style="left:163px"></i><span style="left:152px"></span>
    <i style="left:291px"></i><span style="left:280px"></span>
    <i style="left:421px"></i><span style="left:410px"></span>
    <i style="left:550px"></i><span style="left:539px"></span>
  </section>

  <footer class="footer">
    <section style="height:193px">
      <h5 style="left:143px">About</h5>
      <p class="p abs" style="left:143px;top:70px;width:150px">I am text block. Lorem ipsum dolor sit amet, consectetur adipiscing elit. Ut elit tellus, luctus nec ullamcorper mattis pulvinar leo.</p>
      <div class="soc abs" style="left:143px;top:112px"><i></i><i></i><i></i></div>
      <h5 style="left:369px">Quick Links</h5>
      <ul class="abs" style="left:369px;top:64px"><li>Home</li><li>About Us</li><li>Services</li><li>Contact</li></ul>
      <h5 style="left:513px">Information</h5>
      <ul class="abs" style="left:513px;top:64px;line-height:26px"><li>+1 555 018 2046</li><li>hello@brightwellfs.com</li><li>Street 18 Lakeview, Springfield</li></ul>
    </section>
  </footer>

  <div class="copy">Copyright 2024 © Brightwell Facility Services · All rights reserved</div>

</main>
</body>
</html>
```